Meridale Cleaning Services

In need of a business card design suited for a growing cleaning company.

We offer our cleaning and maintenance services to a wide range of clients including but not limited to the following: constuction industry, hospitality, commercial, industrial and domestic

I want the card to be very noticable, i would like people to say 'hey, great card!' when i hand them my card.double sided would be nice

we want our business to come across as exceedingly professional and innovative (different).

a contemporary design is what we have in mind
we want to present an image of a quality business with a high standard of excellence in consistent service.

i just really need a card that persuades top end quality,
our business is very certified and also strives towards environmentaly friendly alternatives
Updates

hey sorry, i have uploaded my company logo design and name
cheers.

hey guys i have added my company logo/name file on my brief page. many thanks

sorry guys a typo in the brief..
address is Tolley Rd. not Tolly Rd
thanks

Industry/Entity Type

Industrial

Requirements
Must have
• company name: meridale cleaning services
operations manager: Colm Varetti
Tel: (02)9373 6204
Fax: (02)8645 7712
Mob: 0438571490

address: 47 Tolly RD Pymble NSW 2073
Postal Adress: PO Box 5832 North Ryde NSW 2113
email: meridaleclean@wexanet.com.au
website: meridalecleaningservices.com.au

```html
<!DOCTYPE html>
<html lang="en">
<head>
<meta charset="utf-8">
<title>Meridale Cleaning Services – Business Card</title>
<link rel="stylesheet" href="https://fonts.googleapis.com/css2?family=Didact+Gothic&family=Tinos&display=swap">
<style>
  :root {
    --page-bg: #e9e6e1;
    --card-white: #ffffff;
    --card-grey: #eceff1;
    --brand-blue: #1e6fc0;
    --stripe-blue: #3aa9e0;
    --stripe-blue-light: #8fd0f0;
    --stripe-green: #5cbf3a;
    --stripe-green-light: #9ad67e;
    --ink: #1b1b1b;
    --navy-deep: #1d1f6b;
    --navy-mid: #2b3aa0;
    --navy-glow: #2f8be0;
    --white: #ffffff;
    --glow: rgba(170, 215, 255, 0.85);
  }
  * { box-sizing: border-box; margin: 0; padding: 0; }
  html, body {
    width: 958px; height: 1200px; overflow: hidden;
    background: var(--page-bg);
    font-family: "Didact Gothic", "Century Gothic", sans-serif;
  }
  .sheet {
    position: relative; width: 958px; height: 1200px;
  }
  .card {
    position: absolute; left: 59px; width: 840px; height: 470px;
    overflow: hidden;
    box-shadow: 0 10px 28px rgba(0,0,0,0.28);
  }

  /* Front */
  .card--front {
    top: 80px;
    background: radial-gradient(ellipse at 45% 45%, var(--card-white) 0%, var(--card-grey) 100%);
  }
  .card__stripes { position: absolute; inset: 0; width: 840px; height: 470px; }
  .brand {
    position: absolute; left: 105px; top: 95px;
    display: flex; align-items: center; gap: 30px;
  }
  .brand__dot {
    width: 150px; height: 150px; border-radius: 50%;
    background: var(--brand-blue);
  }
  .brand__name {
    color: var(--brand-blue);
    font-weight: 400;
    line-height: 1;
  }
  .brand__name-main { display: block; font-size: 92px; letter-spacing: -1px; }
  .brand__name-sub { display: block; font-size: 33px; letter-spacing: 1px; margin-top: 6px; }
  .contact-web {
    position: absolute; left: 78px; top: 318px;
    font-size: 23px; color: var(--ink); line-height: 1.75;
    transform: rotate(-3deg); transform-origin: left top;
  }

  /* Back */
  .card--back {
    top: 640px;
    background: radial-gradient(ellipse at 50% 45%, var(--navy-glow) 0%, var(--navy-mid) 40%, var(--navy-deep) 85%);
    color: var(--white);
    text-shadow: 0 0 8px var(--glow), 0 0 2px var(--glow);
  }
  .role {
    position: absolute; left: 70px; top: 34px;
    font-size: 34px;
    transform: rotate(2.5deg); transform-origin: left top;
  }
  .role__name { font-family: "Tinos", "Times New Roman", serif; font-size: 36px; }
  .phones {
    position: absolute; left: 290px; top: 150px;
    font-size: 25px; line-height: 1.35;
    transform: rotate(2.5deg); transform-origin: left top;
  }
  .addresses {
    position: absolute; left: 48px; top: 315px;
    font-size: 26px; line-height: 1.35;
    transform: rotate(2.5deg); transform-origin: left top;
  }
</style>
</head>
<body>
<main class="sheet">

  <section class="card card--front" aria-label="Business card front">
    <svg class="card__stripes" viewBox="0 0 840 470" aria-hidden="true">
      <polygon points="40,0 70,0 0,70 0,40" fill="var(--stripe-blue-light)"/>
      <polygon points="95,0 125,0 0,125 0,95" fill="var(--stripe-blue)"/>
      <polygon points="150,0 165,0 0,165 0,150" fill="var(--stripe-blue-light)"/>
      <polygon points="840,330 840,360 730,470 700,470" fill="var(--stripe-green)"/>
      <polygon points="840,385 840,410 780,470 755,470" fill="var(--stripe-green-light)"/>
      <polygon points="840,425 840,450 820,470 795,470" fill="var(--stripe-green)"/>
    </svg>

    <div class="brand">
      <span class="brand__dot" aria-hidden="true"></span>
      <h1 class="brand__name">
        <span class="brand__name-main">Meridale</span>
        <span class="brand__name-sub">CLEANING SERVICES</span>
      </h1>
    </div>

    <p class="contact-web">
      website : www.meridalecleaningservices.com.au<br>
      Email : meridaleclean@wexanet.com.au
    </p>
  </section>

  <section class="card card--back" aria-label="Business card back">
    <p class="role">Operations manager: <span class="role__name">Colm Varetti</span></p>
    <p class="phones">
      Tel: (02)9373 6204<br>
      Fax: (02)8645 7712<br>
      Mob: 0438571490
    </p>
    <p class="addresses">
      Address: 47 Tolley RD Pymble NSW 2073<br>
      Postal Address: PO Box 5832 North Ryde NSW 2113
    </p>
  </section>

</main>
</body>
</html>
```